Q&T Power Outfitters Business Cards

This will be used a business cards. Would love an industrial type flavor paired with the floating/3d is design like attached.

Do not have any certain colors picked out but something that will look good and stand out!!!.

Q&T Power Outfitters
"Power that never sleeps"

The business does home standby Generators..

Contact Information for Business Card

Q&T Power Outfitters

Requirements
Must have
• Would love an industrial type flavor paired with the floating/3d is design like attached for a sample.

```html
<!DOCTYPE html>
<html lang="en">
<head>
<meta charset="utf-8">
<title>Q&amp;T Power Outfitters – Business Cards</title>
<link href="https://fonts.googleapis.com/css2?family=Arimo:wght@400;700&family=Montserrat:wght@600;700&family=Ubuntu:ital,wght@1,500&display=swap" rel="stylesheet">
<style>
  :root {
    --bg: #0d0d0e;
    --card: #2a2b2d;
    --card-back: #262729;
    --edge: #0b4f86;
    --blue: #0a5288;
    --green: #7cc21b;
    --text: #e6e6e6;
    --muted: #bdbdbd;
    --rule: #4a4b4e;
    --emboss: #3b3c3f;
  }
  * { margin: 0; padding: 0; box-sizing: border-box; }
  html, body { width: 1200px; height: 820px; overflow: hidden; background: var(--bg); }
  .canvas {
    width: 1200px; height: 820px; position: relative;
    background: radial-gradient(ellipse at 50% 40%, #1b1b1d 0%, var(--bg) 70%);
  }
  .card {
    position: absolute; top: 255px; width: 525px; height: 300px;
    border-radius: 3px; box-shadow: 0 3px 0 var(--edge), 0 18px 40px rgba(0,0,0,.6);
  }
  .card-front { left: 50px; background: var(--card); }
  .card-back { left: 625px; background: var(--card-back); display: flex; align-items: center; justify-content: center; }

  .brand { position: absolute; top: 46px; right: 60px; text-align: center; }
  .brand-name {
    font-family: "Montserrat", sans-serif; font-weight: 700; font-size: 30px;
    color: var(--blue); letter-spacing: .5px;
  }
  .tagline {
    margin-top: 6px; font-family: "Ubuntu", sans-serif; font-style: italic; font-weight: 500;
    font-size: 19px; color: var(--green);
  }
  .divider { position: absolute; left: 34px; right: 34px; top: 150px; height: 1px; background: var(--rule); }

  .person { position: absolute; left: 34px; top: 166px; }
  .person-name { font-family: "Montserrat", sans-serif; font-weight: 600; font-size: 19px; letter-spacing: .3px; }
  .person-name .first { color: var(--blue); }
  .person-name .last { color: var(--green); }
  .person-role { font-family: "Arimo", sans-serif; font-size: 14px; color: var(--text); margin-top: 2px; }

  .contacts { position: absolute; left: 34px; top: 222px; list-style: none; font-family: "Arimo", sans-serif; font-size: 13px; color: var(--text); }
  .contacts li { display: flex; align-items: center; gap: 8px; height: 21px; }
  .contacts svg { width: 16px; height: 16px; flex: none; }

  .address {
    position: absolute; right: 34px; bottom: 40px; text-align: right; font-style: normal;
    font-family: "Arimo", sans-serif; font-size: 12.5px; line-height: 1.4; color: var(--muted);
  }
  .back-name {
    font-family: "Montserrat", sans-serif; font-weight: 700; font-size: 34px; color: var(--emboss);
  }
</style>
</head>
<body>
<main class="canvas">
  <section class="card card-front" aria-label="Business card front">
    <div class="brand">
      <div class="brand-name">Q&amp;T Power Outfitters</div>
      <div class="tagline">Power that never sleeps</div>
    </div>
    <div class="divider"></div>
    <div class="person">
      <div class="person-name"><span class="first">DANIEL</span> <span class="last">REEVES</span></div>
      <div class="person-role">Managing Director</div>
    </div>
    <ul class="contacts">
      <li>
        <svg viewBox="0 0 16 16" aria-hidden="true"><circle cx="8" cy="8" r="8" fill="#7cc21b"/><path d="M5 4.5c.6-.3 1 .1 1.3.8l.3.8c.1.4-.2.7-.5.9.4 1 1.1 1.8 2 2.3.2-.3.5-.6.9-.5l.8.3c.7.3 1 .7.7 1.3-.4.8-1.2 1-2 .7C6.5 10.4 5.4 9.2 4.6 7.2c-.3-.9-.3-2.2.4-2.7z" fill="#2a2b2d"/></svg>
        044-555 010 220
      </li>
      <li>
        <svg viewBox="0 0 16 16" aria-hidden="true"><circle cx="8" cy="8" r="8" fill="#7cc21b"/><rect x="4" y="5.5" width="8" height="5.5" fill="#2a2b2d"/><path d="M4 5.5l4 3 4-3" fill="none" stroke="#7cc21b" stroke-width=".8"/></svg>
        info@qtpower.com
      </li>
      <li>
        <svg viewBox="0 0 16 16" aria-hidden="true"><circle cx="8" cy="8" r="8" fill="#7cc21b"/><g fill="none" stroke="#2a2b2d" stroke-width=".9"><circle cx="8" cy="8" r="4"/><ellipse cx="8" cy="8" rx="1.8" ry="4"/><path d="M4 8h8M4.6 6h6.8M4.6 10h6.8"/></g></svg>
        www.qtpower.com
      </li>
    </ul>
    <address class="address">17 Foundry Road, Millbrook<br>38810, Eastvale</address>
  </section>

  <section class="card card-back" aria-label="Business card back">
    <div class="back-name">Q&amp;T Power Outfitters</div>
  </section>
</main>
</body>
</html>
```